Business Card Design - Photographer

I am a landscape photographer and I require a business card design. 

I require two designs:
1)  a double sided business card
 and
b)  a single sided business card 

The single sided design can either be the same as the double sided (with just one side having all the information)....or it can be an entire new design. Its up to you.

My corporate colours are (CMYK):

Blue   69, 32, 0, 0
Grey  72,  64,  47,  31
Green  32,  2,  91,  0
Yellow   0, 19, 92, 0
Orange  0, 39, 75, 0

Colour space in final file should be in CMYK.

The details that need to be included on the card:

- Use the provided Logo
- Name: Lukas Wendrovski
- Email:   sales@vistaplume.com.au
- Website:    vistaplume.com.au
- Twitter:    twitter.com/vistaplume
- Facebook:   facebook.com/vistaplume
- Mobile  0415 309 662

Please use the attached template to design the logo to the specified size, including the marked bleed lines. I have also attached my logo in PNG (transparent background) and ai format for you to use.

The final file should be:
- Photoshop version with layers so I can edit the name/text etc. All non vector files should be high resolution at 1039 x 697 pixels at 300 dpi.

I also require a file as:
- Vector based PDF

Anyway questions please contact me.

Thank you

Industry/Entity Type

Landscape

Logo styles of interest
Pictorial/Combination Logo
Abstract Logo
Wordmark Logo
Lettermark Logo
Requirements
Must have
• The details that need to be included on the card:

- Use the provided Logo
- Name: Lukas Wendrovski
- Email: sales@vistaplume.com.au
- Website: vistaplume.com.au
- Twitter: twitter.com/vistaplume
- Facebook: facebook.com/vistaplume
- Mobile 0415 309 662

```html
<!DOCTYPE html>
<html lang="en">
<head>
<meta charset="utf-8">
<title>Vista Plume – Business Cards</title>
<link rel="stylesheet" href="https://fonts.googleapis.com/css2?family=Bebas+Neue&family=Ubuntu:wght@400;500&display=swap">
<style>
  :root {
    --page: #ffffff;
    --card-grey: #ececec;
    --card-white: #ffffff;
    --navy: #253255;
    --ink: #2b3656;
    --label: #111111;
    --shadow: rgba(0, 0, 0, 0.18);
  }
  * { margin: 0; padding: 0; box-sizing: border-box; }
  html, body {
    width: 1200px; height: 1039px; overflow: hidden;
    background: var(--page);
  }
  .sheet { position: relative; width: 1200px; height: 1039px; }
  .section-title {
    position: absolute; left: 45px;
    font-family: "Ubuntu", Arial, sans-serif;
    font-size: 22px; color: var(--label);
  }
  .section-title--double { top: 32px; }
  .section-title--single { top: 578px; }

  .card {
    position: absolute; width: 515px; height: 342px;
    box-shadow: 8px 10px 14px var(--shadow);
    color: var(--ink);
    font-family: "Ubuntu", Arial, sans-serif;
  }
  .card--front  { left: 46px;  top: 141px; background: var(--card-grey); }
  .card--back   { left: 637px; top: 141px; background: var(--card-grey); }
  .card--single { left: 46px;  top: 650px; background: var(--card-white); }
  .card--reverse{ left: 635px; top: 650px; background: var(--navy); }

  .brand {
    position: absolute; left: 0; width: 100%;
    display: flex; flex-direction: column; align-items: center;
  }
  .card--front .brand { top: 118px; }
  .card--single .brand { top: 44px; }
  .brand__dot {
    width: 60px; height: 60px; border-radius: 50%;
    background: var(--navy);
  }
  .brand__name {
    margin-top: 14px;
    font-weight: 500; font-size: 24px; letter-spacing: 3px;
    color: var(--navy); text-transform: uppercase;
  }

  .back-block { position: absolute; left: 50px; top: 44px; }
  .back-block__name {
    font-family: "Bebas Neue", Impact, sans-serif;
    font-size: 46px; line-height: 40px; letter-spacing: 1px;
    color: var(--ink);
  }
  .back-block__role {
    font-family: "Bebas Neue", Impact, sans-serif;
    font-size: 22px; line-height: 22px; letter-spacing: 1px;
    margin-top: 6px;
  }
  .contact { font-size: 14px; line-height: 18px; }
  .back-block .contact { margin-top: 22px; }
  .contact__gap { height: 20px; }

  .single-info {
    position: absolute; left: 0; width: 100%; top: 172px;
    text-align: center;
  }
  .single-info__name { font-size: 22px; font-weight: 500; line-height: 26px; }
  .single-info .contact { font-weight: 500; line-height: 20px; margin-top: 2px; }
  .single-info .contact__gap { height: 16px; }
</style>
</head>
<body>
<main class="sheet">
  <h2 class="section-title section-title--double">1) Double sided business card</h2>

  <section class="card card--front" aria-label="Double sided card, front">
    <div class="brand">
      <span class="brand__dot"></span>
      <span class="brand__name">Vista Plume</span>
    </div>
  </section>

  <section class="card card--back" aria-label="Double sided card, back">
    <div class="back-block">
      <div class="back-block__name">LUKAS<br>WENDROVSKI</div>
      <div class="back-block__role">Landscape Photographer</div>
      <div class="contact">
        <div>0415 309 662</div>
        <div>sales@vistaplume.com.au</div>
        <div class="contact__gap"></div>
        <div>vistaplume.com.au</div>
        <div>twitter.com/vistaplume</div>
        <div>facebook.com/vistaplume</div>
      </div>
    </div>
  </section>

  <h2 class="section-title section-title--single">2) Single sided business card</h2>

  <section class="card card--single" aria-label="Single sided card, front">
    <div class="brand">
      <span class="brand__dot"></span>
      <span class="brand__name">Vista Plume</span>
    </div>
    <div class="single-info">
      <div class="single-info__name">Lukas Wendrovski</div>
      <div class="contact">
        <div>0415 309 662</div>
        <div>sales@vistaplume.com.au</div>
        <div class="contact__gap"></div>
        <div>vistaplume.com.au</div>
        <div>twitter.com/vistaplume</div>
        <div>facebook.com/vistaplume</div>
      </div>
    </div>
  </section>

  <section class="card card--reverse" aria-label="Single sided card, plain reverse"></section>
</main>
</body>
</html>
```